Casa Vero Inspections Business Card

I need a business card for my new company. The company is going to provide home inspections. The name of the company is Casa Vero Inspections. I am not sure if I want a single sided card or a double. I have a logo already that I want to incorporate into the card design. I was wondering if I should incorporate a catch phrase on my card or not. If I did the phrase would be "A Careful Look at Every Home Purchase" but i am unsure how or if to use it on a card. The following information needs to be on the card.
Home Inspection
My Name: Marcus T. Wolford Phone Number: 555-301-7762 Email: mwolford@casaveroinspections.com Website: www.casaveroinspections.com NY HI License # 27300519462

```html
<!DOCTYPE html>
<html lang="en">
<head>
<meta charset="utf-8">
<title>Casa Vero Inspections – Business Card</title>
<link href="https://fonts.googleapis.com/css2?family=Lato:wght@400;700;900&display=swap" rel="stylesheet">
<style>
  :root {
    --page: #e9e7e4;
    --card: #1a1a1b;
    --card-edge: #6ec1ec;
    --accent: #6ec1ec;
    --ink: #ffffff;
    --muted: #d9d9d9;
  }
  * { margin: 0; padding: 0; box-sizing: border-box; }
  html, body { width: 1200px; height: 977px; overflow: hidden; }
  body {
    background: var(--page);
    font-family: "Lato", Arial, sans-serif;
    position: relative;
  }
  .card {
    position: absolute;
    width: 620px;
    height: 354px;
    background: var(--card);
    border-radius: 18px;
    box-shadow: 0 3px 0 var(--card-edge), 0 14px 30px rgba(0,0,0,.25);
    color: var(--ink);
    overflow: hidden;
  }
  .card--front { left: 60px; top: 80px; }
  .card--back { left: 520px; top: 530px; }

  .brand {
    display: flex;
    align-items: center;
    gap: 12px;
  }
  .brand__mark {
    width: 18px; height: 18px;
    background: var(--accent);
    flex: none;
  }
  .brand__name {
    font-weight: 900;
    text-transform: uppercase;
    color: var(--ink);
    letter-spacing: 1px;
    line-height: 1.05;
    white-space: nowrap;
  }

  .card--front .brand {
    position: absolute;
    left: 0; right: 0; top: 120px;
    justify-content: center;
  }
  .card--front .brand__name { font-size: 38px; }
  .tagline {
    position: absolute;
    left: 0; right: 0; top: 250px;
    text-align: center;
    font-size: 18px;
    color: var(--muted);
  }
  .tagline strong { color: var(--accent); font-weight: 700; }

  .card--back .brand {
    position: absolute;
    right: 40px; top: 52px;
  }
  .card--back .brand__name { font-size: 24px; }
  .card--back .brand__mark { width: 12px; height: 12px; }
  .rule {
    position: absolute;
    height: 1.5px;
    background: var(--accent);
  }
  .rule--top { right: 40px; top: 104px; width: 300px; }
  .rule--name { left: 60px; top: 224px; width: 520px; }

  .holder {
    position: absolute;
    left: 60px; top: 180px;
    font-size: 32px;
    font-weight: 900;
    color: var(--accent);
    text-transform: uppercase;
    letter-spacing: .5px;
    white-space: nowrap;
  }
  .contacts {
    position: absolute;
    left: 60px; top: 236px;
    list-style: none;
    font-size: 17px;
    line-height: 29px;
  }
  .contacts li { display: flex; align-items: center; gap: 10px; }
  .contacts svg { width: 14px; height: 14px; fill: var(--accent); flex: none; }

  .license {
    position: absolute;
    right: 40px; top: 132px;
    font-size: 16px;
    line-height: 22px;
  }
  .license__label { color: var(--accent); text-transform: uppercase; }
  .license__number { color: var(--ink); }
</style>
</head>
<body>

<section class="card card--front" aria-label="Card front">
  <div class="brand">
    <span class="brand__mark"></span>
    <span class="brand__name">Casa Vero Inspections</span>
  </div>
  <p class="tagline">A Careful Look at <strong>Every Home Purchase</strong></p>
</section>

<section class="card card--back" aria-label="Card back">
  <div class="brand">
    <span class="brand__mark"></span>
    <span class="brand__name">Casa Vero Inspections</span>
  </div>
  <div class="rule rule--top"></div>

  <div class="license">
    <div class="license__label">NY HI License</div>
    <div class="license__number"># 27300519462</div>
  </div>

  <h1 class="holder">Marcus T. Wolford</h1>
  <div class="rule rule--name"></div>

  <ul class="contacts">
    <li>
      <svg viewBox="0 0 24 24" aria-hidden="true"><path d="M6.6 10.8a15 15 0 0 0 6.6 6.6l2.2-2.2a1 1 0 0 1 1-.25 11.4 11.4 0 0 0 3.6.57 1 1 0 0 1 1 1V20a1 1 0 0 1-1 1A17 17 0 0 1 3 4a1 1 0 0 1 1-1h3.5a1 1 0 0 1 1 1c0 1.25.2 2.45.57 3.57a1 1 0 0 1-.25 1z"/></svg>
      555-301-7762
    </li>
    <li>
      <svg viewBox="0 0 24 24" aria-hidden="true"><path d="M2 5h20v14H2zm2 2v.5l8 5 8-5V7l-8 5z"/></svg>
      mwolford@casaveroinspections.com
    </li>
    <li>
      <svg viewBox="0 0 24 24" aria-hidden="true"><path d="M12 2a10 10 0 1 0 0 20 10 10 0 0 0 0-20zm0 2c1.2 0 2.6 2.3 3 6H9c.4-3.7 1.8-6 3-6zM9 12h6c-.2 4-1.7 8-3 8s-2.8-4-3-8zm-5 0h3c0 3 .7 5.6 1.7 7.3A8 8 0 0 1 4 12zm13 0h3a8 8 0 0 1-4.7 7.3c1-1.7 1.7-4.3 1.7-7.3z"/></svg>
      casaveroinspections.com
    </li>
  </ul>
</section>

</body>
</html>
```